Corvane Solutions Website

Corvane Solutions (CS) provide Analytics & Enterprise Performance Management (EPM) advisory & consultancy services. We are passionate about data and making a difference for our clients by working in partnership with them, helping them on their journey to becoming an Corvane Solution. We deliver insights which give our clients a competitive edge and a much deeper understanding of their organisation.

We need a website which shows who we are, what we do and how we do it.

www.corvane-solutions.com is our very basic website at the moment. We want to completely revamp it with a corporate look

```html
<!DOCTYPE html>
<html lang="en">
<head>
<meta charset="utf-8">
<title>Corvane Solutions</title>
<link href="https://fonts.googleapis.com/css2?family=Montserrat:wght@400;500;600;700;800&family=Michroma&display=swap" rel="stylesheet">
<style>
:root{
  --navy:#2c5269;
  --orange:#e4863f;
  --mist:#e9eef1;
  --ink:#3b3b3b;
  --line:#9fb0bc;
  --white:#ffffff;
}
*{margin:0;padding:0;box-sizing:border-box}
html,body{width:1200px;height:3960px;overflow:hidden}
body{position:relative;background:var(--white);font-family:"Montserrat",sans-serif;color:var(--ink)}
.abs{position:absolute}
.brand{display:flex;align-items:center;gap:10px;color:var(--navy);font-weight:700;font-size:14px;line-height:1.05;letter-spacing:.5px}
.brand-dot{width:38px;height:38px;border-radius:50%;border:6px solid var(--navy)}
.outline{font-family:"Michroma",sans-serif;color:transparent;-webkit-text-stroke:1.4px var(--navy)}
.section-title{position:absolute;left:0;width:1200px;text-align:center;font-size:38px;font-weight:800;color:var(--navy);letter-spacing:.5px}
.section-title .outline{font-weight:400;font-size:34px}
.title-mark{display:block;margin:6px auto 0;width:34px;height:3px;background:var(--navy)}
.btn{position:absolute;background:var(--navy);color:#fff;font-size:13px;font-weight:500;display:flex;align-items:center;justify-content:center;gap:8px;box-shadow:3px 3px 0 -1px #fff,4px 4px 0 0 var(--navy)}
.nav a{position:absolute;top:30px;font-size:12px;font-weight:600;color:var(--navy);text-decoration:none;letter-spacing:.6px}
.body-text{font-size:13.5px;line-height:24.5px;color:var(--ink)}
.service{position:absolute;width:300px;text-align:center}
.service h3{font-size:19px;font-weight:700;color:var(--navy);margin-top:18px}
.service p{font-size:13.5px;line-height:24.5px;margin-top:8px}
.service .more{display:block;margin-top:12px;font-size:13px;font-weight:600;color:var(--orange)}
.circle{position:absolute;width:286px;height:286px;border-radius:50%;border:1.5px solid var(--line);display:flex;align-items:center;justify-content:center;text-align:center;font-size:17px;font-weight:700;color:var(--ink);line-height:21px}
.op{position:absolute;top:2503px;width:20px;height:20px;background:#fff;text-align:center;font-size:16px;line-height:20px;color:var(--ink)}
.partner{position:absolute;top:3467px;width:166px;height:90px;border:1px solid #e3e8ec;background:#fff;display:flex;align-items:center;justify-content:center;box-shadow:0 2px 6px rgba(0,0,0,.05)}
.partner span{width:100px;height:26px;border-radius:4px;background:#c9d3da}
.foot-head{position:absolute;top:3708px;font-size:17px;font-weight:800;color:var(--navy);letter-spacing:.5px}
.foot-link{position:absolute;font-size:12px;color:#555;letter-spacing:.6px}
.contact-row{position:absolute;left:877px;display:flex;gap:14px;align-items:flex-start;color:#fff;font-size:12px;line-height:19px}
.contact-row .ico{width:32px;height:32px;border-radius:50%;border:1.5px solid #fff;display:flex;align-items:center;justify-content:center;flex:none}
</style>
</head>
<body>

<!-- Hero -->
<div class="abs" role="img" aria-label="Robotic hand holding a glowing circuit-board letter mark on a pale lavender background" style="left:0;top:0;width:555px;height:676px;background:linear-gradient(135deg,#eef0f5 0%,#dfe0ec 55%,#c9cbd8 100%)"></div>
<div class="abs brand" style="left:58px;top:15px"><span class="brand-dot"></span><span>CORVANE<br>SOLUTIONS</span></div>
<nav class="nav">
  <a style="left:653px">WHO WE ARE</a>
  <a style="left:793px">WHAT WE DO</a>
  <a style="left:931px">HOW WE DO IT</a>
  <a style="left:1078px">CONTACT</a>
</nav>
<h1 class="abs outline" style="left:597px;top:232px;font-size:62px;line-height:90px;font-weight:400;-webkit-text-stroke:2px var(--navy)">CORVANE<br>SOLUTIONS</h1>
<p class="abs" style="left:599px;top:408px;font-size:23px;font-weight:800;color:#111">DATA ANALYTICS &amp; EPM Consulting Services</p>
<div class="btn" style="left:599px;top:464px;width:205px;height:37px">
  <svg width="14" height="14" viewBox="0 0 24 24" fill="none" stroke="#fff" stroke-width="2"><path d="M22 16.9v3a2 2 0 0 1-2.2 2 19.8 19.8 0 0 1-8.6-3.1 19.5 19.5 0 0 1-6-6A19.8 19.8 0 0 1 2.1 4.2 2 2 0 0 1 4.1 2h3a2 2 0 0 1 2 1.7c.1 1 .4 1.9.7 2.8a2 2 0 0 1-.5 2.1L8 9.9a16 16 0 0 0 6 6l1.3-1.3a2 2 0 0 1 2.1-.4c.9.3 1.8.6 2.8.7a2 2 0 0 1 1.7 2z"/></svg>
  Call On: 01 555 0142</div>

<!-- Who we are -->
<div class="abs" style="left:0;top:676px;width:1200px;height:35px;background:var(--navy);color:#fff;text-align:center;font-size:15px;line-height:35px;letter-spacing:.5px">WELCOME TO CORVANE SOLUTIONS</div>
<div class="abs" style="left:0;top:711px;width:58px;height:549px;background:var(--navy)"></div>
<div class="abs" style="left:0;top:1260px;width:1200px;height:73px;background:var(--mist)"></div>
<h2 class="abs" style="left:98px;top:780px;font-size:36px;font-weight:800;color:var(--navy)">WHO <span class="outline" style="font-size:32px;font-weight:400">WE ARE</span></h2>
<span class="abs" style="left:104px;top:832px;width:34px;height:3px;background:var(--navy)"></span>
<div class="abs body-text" style="left:98px;top:858px;width:452px">
  <p>CS are a Data Analytics &amp; EPM company, specialising in the implementation and support of Business Intelligence, EPM and Data Analytics business solutions, both in the Cloud and on-premise.</p>
  <p style="margin-top:12px">Corvane Solutions is an exciting start-up in the Data Analytics and EPM space.&nbsp; Founded in 2019, CS specialise in the implementation and support of BI, EPM and Data Analytics business solutions, both in the Cloud and on-premise.</p>
</div>
<div class="abs" style="left:98px;top:1094px;width:449px;height:1px;background:#d9d9d9"></div>
<p class="abs" style="left:98px;top:1115px;font-size:13.5px">Call Us On:</p>
<p class="abs" style="left:98px;top:1139px;font-size:16px;font-weight:700;color:var(--orange)">01 555 0142</p>
<div class="abs" style="left:507px;top:1117px;width:40px;height:40px;border-radius:50%;background:var(--orange);display:flex;align-items:center;justify-content:center">
  <svg width="16" height="16" viewBox="0 0 24 24" fill="none" stroke="#fff" stroke-width="2"><path d="M22 16.9v3a2 2 0 0 1-2.2 2 19.8 19.8 0 0 1-8.6-3.1 19.5 19.5 0 0 1-6-6A19.8 19.8 0 0 1 2.1 4.2 2 2 0 0 1 4.1 2h3a2 2 0 0 1 2 1.7c.1 1 .4 1.9.7 2.8a2 2 0 0 1-.5 2.1L8 9.9a16 16 0 0 0 6 6l1.3-1.3a2 2 0 0 1 2.1-.4c.9.3 1.8.6 2.8.7a2 2 0 0 1 1.7 2z"/></svg></div>
<div class="abs" style="left:98px;top:1180px;width:449px;height:1px;background:#d9d9d9"></div>
<div class="abs" role="img" aria-label="Two colleagues working together at a wooden table with a laptop and notebooks" style="left:645px;top:786px;width:450px;height:510px;border-top:6px solid var(--orange);background:linear-gradient(160deg,#6d5f52 0%,#4e4640 50%,#3a3530 100%)"></div>

<!-- What we do -->
<h2 class="section-title" style="top:1400px">WHAT <span class="outline">WE DO</span><span class="title-mark"></span></h2>
<div class="abs" role="img" aria-label="Illustration of a team reviewing large analytics dashboards and charts" style="left:307px;top:1482px;width:553px;height:338px;background:radial-gradient(ellipse at 50% 55%,#c9d2dc 0%,#e3e8ee 55%,#ffffff 80%)"></div>
<div class="abs" style="left:427px;top:1835px;width:344px;height:335px;background:#fff;border-top:3px solid var(--orange);box-shadow:0 6px 22px rgba(0,0,0,.1)"></div>
<div class="service" style="left:82px;top:1880px">
  <svg width="80" height="70" viewBox="0 0 80 70"><circle cx="46" cy="30" r="24" fill="none" stroke="#1f2f3d" stroke-width="4"/><line x1="29" y1="47" x2="12" y2="64" stroke="#1f2f3d" stroke-width="6" stroke-linecap="round"/><polyline points="30,34 40,24 50,32 60,20" fill="none" stroke="#1f2f3d" stroke-width="2"/><circle cx="40" cy="24" r="5" fill="var(--orange)"/><circle cx="50" cy="32" r="5" fill="var(--orange)"/></svg>
  <h3>Analytics</h3>
  <p>Lorem ipsum dolor sit amet, consectetuer adipiscing elit, sed diam nonummy nibh euismod tincidunt ut laoreet dolore magna.</p>
  <span class="more">Read More</span>
</div>
<div class="service" style="left:449px;top:1880px">
  <svg width="90" height="70" viewBox="0 0 90 70"><rect x="0" y="0" width="90" height="70" fill="#dbe8f2"/><rect x="0" y="0" width="90" height="10" fill="#1f2f3d"/><path d="M15 66 A30 30 0 0 1 75 66 Z" fill="#3d6f8c"/><path d="M45 66 L62 30" stroke="var(--orange)" stroke-width="5"/></svg>
  <h3>EPM Advisory</h3>
  <p>Lorem ipsum dolor sit amet, consectetuer adipiscing elit, sed diam nonummy nibh euismod tincidunt ut laoreet dolore magna.</p>
  <span class="more">Read More</span>
</div>
<div class="service" style="left:816px;top:1880px">
  <svg width="80" height="74" viewBox="0 0 80 74"><circle cx="22" cy="8" r="7" fill="#1f2f3d"/><rect x="13" y="17" width="18" height="10" rx="4" fill="#1f2f3d"/><circle cx="58" cy="50" r="7" fill="#1f2f3d"/><rect x="49" y="59" width="18" height="12" rx="5" fill="var(--orange)"/><circle cx="40" cy="40" r="10" fill="#1f2f3d"/><text x="40" y="45" fill="#fff" font-size="13" text-anchor="middle" font-family="Montserrat">?</text><path d="M40 8 H60 V28" fill="none" stroke="#9aa" stroke-width="2"/><path d="M20 36 V64 H40" fill="none" stroke="#9aa" stroke-width="2"/></svg>
  <h3>Consultancy</h3>
  <p>Lorem ipsum dolor sit amet, consectetuer adipiscing elit, sed diam nonummy nibh euismod tincidunt ut laoreet dolore magna.</p>
  <span class="more">Read More</span>
</div>

<!-- How we do it -->
<h2 class="section-title" style="top:2276px">HOW <span class="outline">WE DO IT</span><span class="title-mark"></span></h2>
<div class="circle" style="left:74px;top:2370px">Advise &amp;<br>Architect Services</div>
<div class="circle" style="left:329px;top:2370px">Design &amp;<br>Implement</div>
<div class="circle" style="left:584px;top:2370px">Optimise &amp;<br>Manage</div>
<div class="circle" style="left:839px;top:2370px">Business<br>Improvement</div>
<div class="op" style="left:335px">+</div>
<div class="op" style="left:590px">+</div>
<div class="op" style="left:845px">=</div>
<div class="btn" style="left:516px;top:2688px;width:166px;height:37px">Contact Us Today</div>

<!-- Clients -->
<div class="abs" style="left:1140px;top:2685px;width:60px;height:607px;background:var(--navy)"></div>
<div class="abs" style="left:0;top:2888px;width:58px;height:437px;background:var(--navy)"></div>
<h2 class="section-title" style="top:2831px">WHAT <span class="outline">CLIENTS SAY</span><span class="title-mark"></span></h2>
<div class="abs" style="left:346px;top:2957px;width:734px;height:335px;background:var(--orange)"></div>
<div class="abs" role="img" aria-label="Two colleagues reviewing documents together in a bright office" style="left:120px;top:2918px;width:299px;height:334px;background:linear-gradient(150deg,#b89c86 0%,#8a6b58 55%,#5a4638 100%)"></div>
<p class="abs" style="left:465px;top:2996px;font-size:26px;font-weight:700;color:#fff">Norvik360</p>
<p class="abs" style="left:465px;top:3072px;font-size:16.5px;font-weight:700;color:#fff">Lorem ipsum dolor sit amet, consectetuer adipiscing elit.</p>
<p class="abs" style="left:465px;top:3104px;width:560px;font-size:13px;line-height:24.5px;color:#fff">Lorem ipsum dolor sit amet, consectetuer adipiscing elit, sed diam nonummy nibh euismod tincidunt ut laoreet dolore magna aliquam erat volutpat. Ut wisi enim ad minim veniam, quis nostrud exerci tation ullamcorper suscipit lobortis nisl ut aliquip ex ea commodo consequat.</p>
<p class="abs" style="left:465px;top:3225px;font-size:16.5px;font-weight:700;color:#fff">Marcus Hale, <span style="font-size:11px;font-weight:400">Co Founder</span></p>

<!-- Partners -->
<h2 class="abs" style="left:0;width:1145px;top:3398px;text-align:center;font-size:36px;font-weight:800;color:var(--navy)">OUR <span class="outline" style="font-size:32px;font-weight:400">PARTNERS</span></h2>
<div class="partner" style="left:61px"><span></span></div>
<div class="partner" style="left:244px"><span></span></div>
<div class="partner" style="left:427px"><span></span></div>
<div class="partner" style="left:608px"><span></span></div>
<div class="partner" style="left:791px"><span></span></div>
<div class="partner" style="left:974px"><span></span></div>

<!-- Footer -->
<div class="abs" style="left:0;top:3634px;width:825px;height:29px;background:var(--mist)"></div>
<div class="abs" style="left:0;top:3652px;width:58px;height:308px;background:var(--navy)"></div>
<div class="abs" style="left:825px;top:3634px;width:375px;height:326px;background:var(--orange);overflow:hidden">
  <div style="position:absolute;left:150px;top:40px;width:300px;height:300px;border-radius:50%;border:50px solid rgba(255,255,255,.08)"></div>
</div>
<div class="abs brand" style="left:120px;top:3710px"><span class="brand-dot"></span><span>CORVANE<br>SOLUTIONS</span></div>
<p class="abs" style="left:120px;top:3780px;font-size:11px;line-height:19px;color:#333">© <b style="color:var(--navy)">CORVANE SOLUTIONS</b> -<br>2022. All rights reserved.</p>
<p class="foot-head" style="left:410px">QUICK LINKS</p>
<p class="foot-link" style="left:410px;top:3750px">WHO WE ARE</p>
<p class="foot-link" style="left:410px;top:3780px">WHAT WE DO</p>
<p class="foot-link" style="left:410px;top:3810px">HOW WE DO IT</p>
<p class="foot-link" style="left:410px;top:3840px">CONTACT</p>
<p class="foot-head" style="left:600px">FOLLOW US ON</p>
<p class="foot-link" style="left:600px;top:3750px">CONNECTLY</p>
<p class="foot-link" style="left:600px;top:3780px">CHIRPLINE</p>
<p class="foot-head" style="left:877px;color:#fff">CONTACT DETAILS</p>
<div class="contact-row" style="top:3746px">
  <span class="ico"><svg width="14" height="14" viewBox="0 0 24 24" fill="none" stroke="#fff" stroke-width="2"><path d="M12 22s7-7 7-12a7 7 0 0 0-14 0c0 5 7 12 7 12z"/><circle cx="12" cy="10" r="2.5"/></svg></span>
  <span style="margin-top:-6px">14 Harbour Row,<br>Eastgate, Dublin 4,<br>D04 KT21</span>
</div>
<div class="contact-row" style="top:3814px">
  <span class="ico"><svg width="14" height="14" viewBox="0 0 24 24" fill="none" stroke="#fff" stroke-width="2"><path d="M22 16.9v3a2 2 0 0 1-2.2 2 19.8 19.8 0 0 1-8.6-3.1 19.5 19.5 0 0 1-6-6A19.8 19.8 0 0 1 2.1 4.2 2 2 0 0 1 4.1 2h3a2 2 0 0 1 2 1.7c.1 1 .4 1.9.7 2.8a2 2 0 0 1-.5 2.1L8 9.9a16 16 0 0 0 6 6l1.3-1.3a2 2 0 0 1 2.1-.4c.9.3 1.8.6 2.8.7a2 2 0 0 1 1.7 2z"/></svg></span>
  <span style="margin-top:6px;font-size:13px">01 555 0142</span>
</div>
<div class="contact-row" style="top:3863px">
  <span class="ico"><svg width="14" height="14" viewBox="0 0 24 24" fill="none" stroke="#fff" stroke-width="2"><rect x="3" y="5" width="18" height="14" rx="2"/><path d="M3 7l9 6 9-6"/></svg></span>
  <span style="margin-top:6px">info@corvane-solutions.com</span>
</div>

</body>
</html>
```